All Natural Dog Treat Website

Hello!

We need a website designed for the all natural, made in the U.S.A. dog treats we produce.

Our customer is a bit more upscale and knowledgeable about what the purchase for their pet.

We aren't big on stock photos, preference is for either no photos or a cartoon type graphic on the site.

The site is not an ecommerce site, it's basically a place for information and then a link is needed to direct people over to shopvarlo.com to make a purchase.

The site would consist of a main page, an about us page, a page tht has the benefits of our healthy treats and then a Wholesale Page, that has our contact info for companies wishing to carry our treats to contact us.

Looking for something very clean and contemporary and creative.

Our company is named Granny Pell's Dog Treats. Attached is our label that goes on our product.

```html
<!DOCTYPE html>
<html lang="en">
<head>
<meta charset="utf-8">
<title>Granny Pell's Dog Treats</title>
<link rel="stylesheet" href="https://fonts.googleapis.com/css2?family=Bebas+Neue&family=Montserrat:wght@300;700&family=Oswald:wght@300&family=PT+Sans:wght@400;700&display=swap">
<style>
  :root {
    --orange: #f3892b;
    --orange-panel: #f38a2c;
    --orange-deep: #d4470f;
    --orange-dark: #bf3a04;
    --brown: #8e3d17;
    --page-grey: #f5f5f5;
    --white: #ffffff;
    --ink: #333333;
    --ink-soft: #777777;
    --nav-active: #e8521a;
    --rule: #ececec;
  }
  * { box-sizing: border-box; margin: 0; padding: 0; }
  html, body { width: 688px; height: 1200px; overflow: hidden; }
  body { font-family: Arial, Helvetica, sans-serif; background: var(--page-grey); }
  h1, h2, h3, h4 { font-weight: 400; }
  .canvas { position: relative; width: 688px; height: 1200px; overflow: hidden; background: var(--page-grey); }
  .abs { position: absolute; }

  /* Top band */
  .top-band { left: 0; top: 0; width: 688px; height: 413px; background: var(--orange); }
  .hero-column { left: 82px; top: 43px; width: 525px; height: 254px; background: var(--orange-panel);
    box-shadow: 0 0 14px rgba(120,50,0,.28); }
  .site-header { left: 82px; top: 43px; width: 525px; height: 65px; background: var(--white); }
  .brand { left: 12px; top: 20px; display: flex; align-items: center; gap: 8px;
    font-family: "PT Sans", sans-serif; font-weight: 700; font-size: 21px; color: var(--orange-deep); white-space: nowrap; }
  .brand-dot { width: 14px; height: 14px; border-radius: 50%; background: var(--orange-deep); }
  .main-nav { left: 0; top: 25px; width: 525px; height: 16px; font-family: "Bebas Neue", sans-serif; font-size: 14px; letter-spacing: .2px; color: #2e2e2e; }
  .main-nav a { position: absolute; top: 0; color: inherit; text-decoration: none; white-space: nowrap; }
  .main-nav a.is-active { color: var(--nav-active); }

  .mascot-art { left: 103px; top: 116px; width: 125px; height: 164px; border-radius: 40px;
    background: radial-gradient(circle at 50% 50%, rgba(255,255,255,.30), rgba(255,255,255,.12)); }
  .hero-title { left: 228px; top: 148px; width: 359px; text-align: right; font-family: "Montserrat", sans-serif;
    font-size: 41px; line-height: 44px; color: var(--white); letter-spacing: 1.5px; white-space: nowrap; }
  .hero-title .light { font-weight: 300; }
  .hero-title .bold { font-weight: 700; }
  .hero-subtitle { left: 230px; top: 188px; width: 357px; text-align: right; font-family: "Oswald", sans-serif;
    font-weight: 300; font-size: 16px; color: var(--white); letter-spacing: .6px; white-space: nowrap; }
  .hero-product { left: 279px; top: 224px; width: 200px; height: 40px; border-top: 2px solid var(--white);
    border-bottom: 2px solid var(--white); text-align: center; font-family: "Montserrat", sans-serif;
    font-weight: 300; font-size: 27px; line-height: 36px; color: var(--white); letter-spacing: .5px; white-space: nowrap; }

  /* Feature tabs */
  .tabs-shadow { left: 110px; top: 404px; width: 470px; height: 20px; border-radius: 50%;
    background: radial-gradient(ellipse at center, rgba(0,0,0,.18), rgba(0,0,0,0) 70%); }
  .feature-tab { top: 297px; height: 116px; color: var(--white); text-align: center;
    background: radial-gradient(circle at 50% 45%, #e2581b, var(--orange-dark) 80%); }
  .feature-tab.is-left { left: 102px; width: 160px; }
  .feature-tab.is-right { left: 427px; width: 160px; }
  .feature-tab.is-current { left: 262px; top: 292px; width: 165px; height: 135px;
    background: radial-gradient(circle at 50% 42%, #f9a25a, #ef7f22 65%); box-shadow: 0 2px 8px rgba(0,0,0,.2); }
  .tab-label { position: absolute; left: 0; width: 100%; top: 69px; font-family: "Bebas Neue", sans-serif; font-size: 19px; white-space: nowrap; }
  .tab-icon { position: absolute; left: 50%; top: 40px; transform: translateX(-50%); }
  .tab-mark { position: absolute; left: 63px; top: 26px; width: 40px; height: 40px; border-radius: 50%; background: var(--white); }
  .tab-heading { position: absolute; left: 0; width: 100%; top: 70px; font-family: "PT Sans", sans-serif; font-size: 19px; line-height: 23px; }

  .slider-dots { left: 329px; top: 445px; display: flex; gap: 3px; }
  .slider-dots span { width: 8px; height: 8px; border-radius: 50%; background: #f0a219; }
  .slider-dots span.is-active { background: var(--orange-deep); }

  /* Intro cards */
  .intro-cards { left: 101px; top: 469px; width: 487px; height: 142px; background: var(--white);
    border: 1px solid #eeeeee; box-shadow: 0 6px 8px -6px rgba(0,0,0,.12); }
  .intro-card { position: absolute; top: 0; height: 142px; }
  .intro-card + .intro-card { border-left: 1px solid var(--rule); }
  .card-heading { position: absolute; top: 17px; font-family: "PT Sans", sans-serif; font-size: 12.5px; color: var(--ink); white-space: nowrap; }
  .card-text { position: absolute; top: 46px; width: 100px; font-size: 7.3px; line-height: 12.4px; color: var(--ink-soft); }
  .read-more { top: 595px; width: 65px; height: 21px; background: linear-gradient(#e0541a, #c93f0a);
    color: var(--white); font-size: 8px; line-height: 21px; text-align: center; box-shadow: 0 2px 3px rgba(0,0,0,.25); }

  .section-title { left: 101px; top: 634px; font-family: "PT Sans", sans-serif; font-size: 12px; color: var(--ink); }
  .about-box { left: 101px; top: 675px; width: 487px; height: 213px; background: var(--white); border: 1px solid #eeeeee; }
  .about-heading { left: 28px; top: 44px; width: 200px; font-family: "PT Sans", sans-serif; font-size: 13.5px; line-height: 19px; color: var(--orange-deep); }
  .about-text { font-size: 7.2px; line-height: 12.5px; color: var(--ink-soft); }
  .about-text.is-left { left: 28px; top: 86px; width: 206px; }
  .about-text.is-right { left: 256px; top: 46px; width: 206px; }

  /* Footer */
  .site-footer { left: 0; top: 916px; width: 688px; height: 224px; background: var(--white); }
  .footer-heading { position: absolute; top: 26px; font-family: "Bebas Neue", sans-serif; font-size: 11.5px; color: var(--ink); white-space: nowrap; }
  .footer-links { position: absolute; top: 55px; list-style: none; font-size: 7.5px; line-height: 16.3px; color: var(--ink-soft); }
  .footer-blurb { position: absolute; left: 292px; top: 55px; width: 135px; font-size: 7.3px; line-height: 13px; color: var(--ink-soft); }
  .contact-line { position: absolute; left: 494px; font-size: 7.3px; line-height: 13px; color: var(--ink-soft); white-space: nowrap; }
  .contact-icon { position: absolute; left: 478px; }

  .social-bar { left: 271px; top: 1121px; width: 148px; height: 24px; background: var(--brown);
    display: flex; align-items: center; justify-content: center; gap: 10px; box-shadow: 0 2px 3px rgba(0,0,0,.3); }
  .social-bar span { width: 7px; height: 7px; border-radius: 50%; background: #c9a08a; }
  .bottom-bar { left: 0; top: 1140px; width: 688px; height: 60px; background: var(--orange); }
  .copyright { position: absolute; left: 0; top: 22px; width: 100%; text-align: center; font-family: "PT Sans", sans-serif; font-size: 8px; color: var(--white); }
</style>
</head>
<body>
<div class="canvas">
  <div class="abs top-band"></div>
  <div class="abs hero-column"></div>

  <header class="abs site-header">
    <div class="abs brand"><span class="brand-dot"></span>Granny Pell's</div>
    <nav class="abs main-nav">
      <a class="is-active" style="left:248px">Home</a>
      <a style="left:301px">About Us</a>
      <a style="left:368px">Our Products</a>
      <a style="left:455px">Contact</a>
    </nav>
  </header>

  <div class="abs mascot-art" role="img" aria-label="Cartoon dog mascot artwork"></div>
  <h1 class="abs hero-title"><span class="light">ALL </span><span class="bold">NATURAL</span></h1>
  <p class="abs hero-subtitle">WE USE HUMAN GRADE FOOD</p>
  <p class="abs hero-product">DOG TREATS</p>

  <div class="abs tabs-shadow"></div>
  <div class="abs feature-tab is-left">
    <svg class="tab-icon" width="18" height="22" viewBox="0 0 18 22" aria-hidden="true">
      <circle cx="9" cy="8" r="7" fill="#fff" stroke="#7a2a05" stroke-width="1.5"/>
      <rect x="6" y="14" width="6" height="5" fill="#fff"/>
    </svg>
    <div class="tab-label">Unique Thinking</div>
  </div>
  <div class="abs feature-tab is-right">
    <svg class="tab-icon" width="24" height="20" viewBox="0 0 24 20" aria-hidden="true">
      <path d="M2 18 L18 5 M10 3 L21 2 L20 12 Z" stroke="#fff" stroke-width="3" fill="#fff"/>
    </svg>
    <div class="tab-label">Great Way</div>
  </div>
  <div class="abs feature-tab is-current">
    <div class="tab-mark" role="img" aria-label="Brand mascot mark"></div>
    <div class="tab-heading">We Use Human<br>Grade Food</div>
  </div>

  <div class="abs slider-dots"><span></span><span></span><span class="is-active"></span></div>

  <section class="abs intro-cards">
    <div class="intro-card" style="left:0;width:166px">
      <h2 class="card-heading" style="left:31px">Heading One</h2>
      <p class="card-text" style="left:31px">Lorem ipsum dolor sit amet, co sectetur lorem adipiscing elit. Mauris imperdiet neque arcu. Vestibulum nec ante eget enim adipiscing dapibus vel sit amet massa.</p>
    </div>
    <div class="intro-card" style="left:166px;width:157px">
      <h2 class="card-heading" style="left:24px">Heading Two</h2>
      <p class="card-text" style="left:24px">Lorem ipsum dolor sit amet, co sectetur lorem adipiscing elit. Mauris imperdiet neque arcu. Vestibulum nec ante eget enim adipiscing dapibus vel sit amet massa.</p>
    </div>
    <div class="intro-card" style="left:323px;width:163px">
      <h2 class="card-heading" style="left:24px">Heading Three</h2>
      <p class="card-text" style="left:24px">Lorem ipsum dolor sit amet, co sectetur lorem adipiscing elit. Mauris imperdiet neque arcu. Vestibulum nec ante eget enim adipiscing dapibus vel sit amet massa.</p>
    </div>
  </section>
  <a class="abs read-more" style="left:150px">Read more</a>
  <a class="abs read-more" style="left:313px">Read more</a>
  <a class="abs read-more" style="left:476px">Read more</a>

  <h2 class="abs section-title">About Us</h2>
  <section class="abs about-box">
    <h3 class="abs about-heading">Sed suscipit lorem ipsum dolor sit amet lorem ipsum</h3>
    <p class="abs about-text is-left">Lorem ipsum dolor sit amet, consectetur adipiscing elit. Proin eget velit nisl. Nulla semper velit vitae libero faucibus. Lorem ipsum dolor sit amet, consectetur adipiscing elit. Lorem ipsum dolor sit amet, consectetur adipiscing elit. Proin eget velit nisl. Nulla semper velit vitae libero faucibus. Lorem ipsum dolor sit amet, consectetur adipiscing elit. Proin eget velit nisl. Nulla semper velit vitae libero faucibus. Lorem ipsum dolor sit amet, consectetur adipiscing elit. Proin eget velit nisl.</p>
    <p class="abs about-text is-right">Lorem ipsum dolor sit amet, consectetur adipiscing elit. Proin eget velit nisl. Nulla semper velit vitae libero faucibus. Lorem ipsum dolor sit amet, consectetur adipiscing elit. Nulla semper velit vitae libero faucibus. Lorem ipsum dolor sit amet, consectetur adipiscing elit. Lorem ipsum dolor sit amet, consectetur adipiscing elit. Proin eget velit nisl. Nulla semper velit vitae libero faucibus. Lorem ipsum dolor sit amet, consectetur adipiscing elit. Proin eget velit nisl. Nulla semper velit vitae libero faucibus. Lorem ipsum dolor sit amet, consectetur adipiscing elit. Proin eget velit nisl.</p>
  </section>

  <footer class="abs site-footer">
    <h4 class="footer-heading" style="left:101px">Nav Links</h4>
    <ul class="footer-links" style="left:101px">
      <li>About us</li><li>Blog</li><li>Contact</li><li>Home</li><li>Portfolio</li><li>Services</li>
    </ul>
    <h4 class="footer-heading" style="left:192px">Useful Links</h4>
    <ul class="footer-links" style="left:192px">
      <li>Carrer</li><li>FAQ</li><li>Marketing</li><li>Privacy</li><li>Terms of use</li>
    </ul>
    <h4 class="footer-heading" style="left:292px">Granny Pell's Dog Treats</h4>
    <p class="footer-blurb">Lorem ipsum dolor sit amet, conse ctetur adipiscing elit. Proin eget velit nisl. Nulla semper velit vitae libero faucibus mollis. Vivamus ut arcu nisi, a cursus orci. Vivamus ut arcu nisi, a cursus orci.</p>
    <h4 class="footer-heading" style="left:477px">Contact Us</h4>
    <svg class="contact-icon" style="top:58px" width="9" height="11" viewBox="0 0 9 11" aria-hidden="true">
      <path d="M4.5 0 A3.5 3.5 0 0 1 8 3.5 C8 6 4.5 11 4.5 11 C4.5 11 1 6 1 3.5 A3.5 3.5 0 0 1 4.5 0 Z" fill="#e0541a"/>
      <circle cx="4.5" cy="3.5" r="1.3" fill="#fff"/>
    </svg>
    <p class="contact-line" style="top:56px">52 Maple Orchard Lane<br>Your street, 1000 Ohio</p>
    <svg class="contact-icon" style="top:92px" width="10" height="8" viewBox="0 0 10 8" aria-hidden="true">
      <path d="M0 2 Q5 -1 10 2 L9 3.5 L7 2.8 L7 4 L9 5 L9 8 L1 8 L1 5 L3 4 L3 2.8 L1 3.5 Z" fill="#e0541a"/>
    </svg>
    <p class="contact-line" style="top:91px">Phone: +1 555 0142 77<br>Fax: +1 555 0142 78</p>
    <svg class="contact-icon" style="top:118px" width="10" height="7" viewBox="0 0 10 7" aria-hidden="true">
      <rect width="10" height="7" fill="#e0541a"/><path d="M0 0 L5 4 L10 0" stroke="#fff" stroke-width="1" fill="none"/>
    </svg>
    <p class="contact-line" style="top:116px">hello@grannypell.com<br>Web: www.grannypell.com</p>
  </footer>

  <div class="abs bottom-bar"><p class="copyright">All Rights Reserved. 2013</p></div>
  <div class="abs social-bar" aria-label="Social links">
    <span></span><span></span><span></span><span></span><span></span><span></span>
  </div>
</div>
</body>
</html>
```